Kestrel Plumbing business card full re design & logo design

Kestrel Plumbing is a Sydney based mechanical plumbing contractor company.
We would like a full redesign with new logo etc which we can take to a future website, uniforms, vehicle sign writing etc.
Blue is my preferred choice of colour but i would be open to see a couple of alternatives thrown in the mix to see how they compare. I am open to see on white cards, black cards etc. Open to many new ideas.
Please see attached original business cards which have been used for the last 5 years.

Target Market(s)

Mechanical services industry.

Industry/Entity Type

Plumbing

Contact Information for Business Card

Dale Fenmore
Director

Mob: 0427 596 418
Email: dale@kestrelplumbing-demo.net.au
PO BOX 782
Larkfield NSW 2199
Lic: 518604k

Logo Text

Kestrel Plumbing

Font styles to use
Sans Serif

Colors
0655a3
3276b5
0792cd
33a6d7
85cae6
000000
333333
474747

Requirements
Must have
• Things that make it very professional and very well presented.
Nice to have
• Same description or very similar to attached uploaded file
Should not have
• Anything that makes it look unprofessional or cartoony.

```html
<!DOCTYPE html>
<html lang="en">
<head>
<meta charset="utf-8">
<title>Kestrel Plumbing – Business Card</title>
<link rel="stylesheet" href="https://fonts.googleapis.com/css2?family=Open+Sans:wdth,wght@75..100,300..700&display=swap">
<style>
  :root {
    --navy: #0f3a66;
    --navy-deep: #0b2f55;
    --brand: #2a5f93;
    --sky: #85cae6;
    --sky-mid: #6fa9cc;
    --white: #ffffff;
    --grey-text: #5a7590;
    --stage: #e8ebef;
  }
  * { box-sizing: border-box; margin: 0; padding: 0; }
  html, body { width: 1200px; height: 900px; overflow: hidden; }
  body {
    background: var(--stage);
    font-family: "Open Sans", Arial, sans-serif;
    position: relative;
  }
  .card {
    position: absolute;
    background: var(--white);
    overflow: hidden;
    box-shadow: 0 6px 18px rgba(0,0,0,0.18);
  }
  .card-shape { position: absolute; inset: 0; }

  /* Front */
  .card-front { left: 60px; top: 273px; width: 620px; height: 354px; }
  .front-brand {
    position: absolute; left: 0; right: 0; top: 58px;
    text-align: center;
  }
  .brand-name {
    display: inline-flex; align-items: center; gap: 10px;
    font-size: 32px; font-weight: 500; color: var(--brand);
    letter-spacing: 0.5px;
  }
  .brand-mark { width: 14px; height: 14px; background: var(--brand); }
  .brand-tagline {
    margin-top: 4px;
    font-size: 13px; letter-spacing: 3px; color: var(--grey-text);
  }
  .person {
    position: absolute; right: 320px; top: 228px;
    text-align: right; color: var(--white);
  }
  .person-name { font-size: 19px; font-weight: 500; }
  .person-role { font-size: 17px; margin-top: -2px; }
  .person-licence { font-size: 14px; margin-top: 14px; }
  .divider {
    position: absolute; left: 318px; top: 205px;
    width: 1px; height: 112px; background: var(--white);
  }
  .contacts {
    position: absolute; left: 336px; top: 186px;
    list-style: none; color: var(--white); font-size: 13.5px;
  }
  .contact { display: flex; align-items: flex-start; gap: 10px; margin-bottom: 4px; }
  .contact-icon { width: 14px; height: 14px; flex: none; margin-top: 2px; }
  .contact-lines { line-height: 1.2; }

  /* Back */
  .card-back { left: 780px; top: 140px; width: 354px; height: 620px; }
  .back-brand {
    position: absolute; right: 34px; top: 56px; text-align: right;
  }
  .back-brand .brand-name { font-size: 28px; }
  .back-tagline {
    margin-top: 18px; font-size: 20px; font-weight: 300;
    color: var(--sky-mid); line-height: 1.1;
  }
  .back-tagline-spaced { letter-spacing: 11px; margin-right: -11px; }
  .services {
    position: absolute; right: 34px; top: 300px;
    text-align: right; color: var(--white);
    font-stretch: 80%;
  }
  .services-area {
    font-size: 20px; font-weight: 400; color: var(--sky);
    letter-spacing: 1.5px; line-height: 1.25;
  }
  .services-heading {
    margin-top: 18px; font-size: 21px; font-weight: 700; letter-spacing: 0.5px;
  }
  .services-list {
    list-style: none; margin-top: 6px;
    font-size: 22px; font-weight: 300; line-height: 1.28;
  }
</style>
</head>
<body>

<section class="card card-front" aria-label="Business card front">
  <svg class="card-shape" width="620" height="354" viewBox="0 0 620 354" aria-hidden="true">
    <defs>
      <linearGradient id="band-front" x1="0" y1="0" x2="1" y2="0">
        <stop offset="0" stop-color="#0b2f55"/>
        <stop offset="1" stop-color="#1d4e80"/>
      </linearGradient>
    </defs>
    <path d="M0,188 Q330,196 620,128 L620,354 L0,354 Z" fill="#85cae6"/>
    <path d="M0,196 Q330,204 620,136 L620,354 L0,354 Z" fill="url(#band-front)"/>
  </svg>

  <div class="front-brand">
    <div class="brand-name"><span class="brand-mark"></span>Kestrel Plumbing</div>
    <div class="brand-tagline">Mechanical Plumbing Solutions</div>
  </div>

  <div class="person">
    <div class="person-name">Dale Fenmore</div>
    <div class="person-role">Director</div>
    <div class="person-licence">Lic: 518604k</div>
  </div>

  <div class="divider"></div>

  <ul class="contacts">
    <li class="contact">
      <svg class="contact-icon" viewBox="0 0 14 14" aria-hidden="true">
        <circle cx="7" cy="7" r="7" fill="#fff"/>
        <path d="M7 3a2.6 2.6 0 0 0-2.6 2.6C4.4 7.6 7 11 7 11s2.6-3.4 2.6-5.4A2.6 2.6 0 0 0 7 3z" fill="#0f3a66"/>
        <circle cx="7" cy="5.6" r="1" fill="#fff"/>
      </svg>
      <span class="contact-lines">PO BOX 782<br>Larkfield NSW 2199</span>
    </li>
    <li class="contact">
      <svg class="contact-icon" viewBox="0 0 14 14" aria-hidden="true">
        <circle cx="7" cy="7" r="7" fill="#fff"/>
        <path d="M4.6 3.6l1.4-.3.8 1.9-.9.7a5 5 0 0 0 2.2 2.2l.7-.9 1.9.8-.3 1.4c-3.4.3-6.1-2.4-5.8-5.8z" fill="#0f3a66"/>
      </svg>
      <span class="contact-lines">0427 596 418</span>
    </li>
    <li class="contact">
      <svg class="contact-icon" viewBox="0 0 14 14" aria-hidden="true">
        <circle cx="7" cy="7" r="7" fill="#fff"/>
        <rect x="3.5" y="4.5" width="7" height="5" fill="#0f3a66"/>
        <path d="M3.5 4.5L7 7.3l3.5-2.8" stroke="#fff" stroke-width="0.8" fill="none"/>
      </svg>
      <span class="contact-lines">dale@kestrelplumbing-demo.net.au</span>
    </li>
  </ul>
</section>

<section class="card card-back" aria-label="Business card back">
  <svg class="card-shape" width="354" height="620" viewBox="0 0 354 620" aria-hidden="true">
    <defs>
      <linearGradient id="band-back" x1="0" y1="0" x2="0" y2="1">
        <stop offset="0" stop-color="#13406f"/>
        <stop offset="1" stop-color="#0b2f55"/>
      </linearGradient>
    </defs>
    <path d="M0,250 Q190,236 354,164 L354,620 L0,620 Z" fill="#85cae6"/>
    <path d="M0,258 Q190,244 354,172 L354,620 L0,620 Z" fill="url(#band-back)"/>
  </svg>

  <div class="back-brand">
    <div class="brand-name"><span class="brand-mark"></span>Kestrel Plumbing</div>
    <div class="back-tagline">
      <div>Mechanical Plumbing</div>
      <div class="back-tagline-spaced">Services</div>
    </div>
  </div>

  <div class="services">
    <div class="services-area">MECHANICAL&nbsp; PIPING</div>
    <div class="services-area">CHW|HW|CW|REFRIG</div>
    <div class="services-heading">SPECIALISING IN</div>
    <ul class="services-list">
      <li>Make good</li>
      <li>Refurbishment</li>
      <li>Tenancy Fit out</li>
      <li>Plant room works</li>
      <li>Shut Downs</li>
      <li>Change overs</li>
    </ul>
  </div>
</section>

</body>
</html>
```